Interactive medical research website - INFOGRAPHIC

We are a non-profit developing TrialSprint, the world's first online, interactive website dedicated to repurposing research (medical research using existing drugs, devices, and nutriceuticals to create new treatments) , and launching in beta at the end of the month. We need an infographic showing the flow of TrialSprint for use on web and print materials introducing the site.

In the attached document, I provide the information we want represented, which is basically: what goes in, what happens, what comes out, and the ultimate goal. This could be represented in any number of ways through metaphor (a machine, and spinning top, etc) and would ideally show speed or acceleration as a part of the process.

Specific colors already in use are on document as well. Fonts are: century gothic (for print) and proximal (for web) - either would be fine.
Updates

Hi Designers - would love to receive your ideas today! Thank you!

Target Market(s)

science, philanthropy, healthcare industry

Industry/Entity Type

Non-Profit

Requirements
Must have
• clear flow, excitement
• use colors from attached document
Nice to have
• a good metaphor - TrialSprintTM as a hub, an actual accelerator, an action tank of some kind

```html
<!DOCTYPE html>
<html lang="en">
<head>
<meta charset="utf-8">
<title>TrialSprint – How It Works</title>
<link rel="stylesheet" href="https://fonts.googleapis.com/css2?family=Lato:wght@300;400;700&display=swap">
<style>
  :root {
    --bg: #f4f4f4;
    --ink: #3a3a3a;
    --ink-soft: #555555;
    --rule: #bdbdbd;
    --icon-bg: #e3e3e3;
    --icon-ink: #5a5a5a;
    --brand: #4a6d86;
    --purple: #7b2b8c;
    --blue: #2e4c9e;
    --pink: #e0186f;
    --orange: #f7941d;
    --lime: #c4dc6c;
    --teal: #1ea8a6;
    --navy: #1e3f86;
    --forest: #1f3a2c;
    --spark: #f28a1e;
  }
  * { box-sizing: border-box; margin: 0; padding: 0; }
  html, body { width: 1200px; height: 680px; overflow: hidden; background: var(--bg); }
  body { font-family: "Lato", Arial, sans-serif; color: var(--ink); }
  .canvas { position: relative; width: 1200px; height: 680px; }
  .flow { position: absolute; inset: 0; }
  .brand { position: absolute; left: 140px; top: 168px; display: flex; align-items: center; }
  .brand-dot { width: 64px; height: 64px; border-radius: 50%; background: var(--brand); }
  .brand-rule { width: 1px; height: 40px; background: var(--rule); margin: 0 10px 0 14px; }
  .brand-name { font-size: 19px; font-weight: 400; letter-spacing: 0.5px; color: var(--brand); text-transform: uppercase; }
  .stage-title { position: absolute; font-weight: 300; font-size: 18px; letter-spacing: 0.5px; color: var(--ink); }
  .input-title { position: absolute; font-weight: 700; font-size: 12px; line-height: 13px; text-align: center; color: var(--ink); text-transform: uppercase; width: 120px; }
  .note { position: absolute; font-size: 10.5px; line-height: 12.3px; color: var(--ink-soft); }
  .note-list { list-style: none; }
  .note-list li { padding-left: 0; }
</style>
</head>
<body>
<main class="canvas">
  <svg class="flow" width="1200" height="680" viewBox="0 0 1200 680" aria-hidden="true">
    <!-- guide rules -->
    <line x1="60" y1="345" x2="285" y2="345" stroke="var(--rule)" stroke-width="0.6"/>
    <line x1="352" y1="345" x2="580" y2="345" stroke="var(--rule)" stroke-width="0.6"/>
    <polyline points="18,440 666,440 666,380" fill="none" stroke="var(--rule)" stroke-width="1.5"/>
    <!-- people bullet rule -->
    <line x1="20" y1="440" x2="20" y2="592" stroke="var(--rule)" stroke-width="0.8"/>
    <!-- input stems -->
    <g stroke="var(--rule)" stroke-width="0.8">
      <line x1="190" y1="470" x2="190" y2="482"/>
      <line x1="315" y1="470" x2="315" y2="482"/>
      <line x1="438" y1="470" x2="438" y2="482"/>
      <line x1="562" y1="470" x2="562" y2="482"/>
    </g>
    <!-- output bracket -->
    <polyline points="888,88 888,224 1012,224 1012,256" fill="none" stroke="var(--rule)" stroke-width="0.8"/>
    <line x1="842" y1="378" x2="842" y2="396" stroke="var(--rule)" stroke-width="0.8"/>
    <line x1="1075" y1="378" x2="1075" y2="396" stroke="var(--rule)" stroke-width="0.8"/>
    <!-- connector lines -->
    <g stroke="var(--rule)" stroke-width="0.8">
      <line x1="740" y1="282" x2="786" y2="218"/>
      <line x1="786" y1="218" x2="818" y2="215"/>
      <line x1="840" y1="230" x2="840" y2="280"/>
      <line x1="1098" y1="278" x2="1118" y2="283"/>
    </g>

    <!-- accelerator track -->
    <g fill="none" stroke-width="28">
      <path d="M666 380 V315 A58 58 0 0 1 782 315" stroke="var(--purple)"/>
      <path d="M782 315 A58 58 0 0 0 898 315" stroke="var(--blue)"/>
      <path d="M898 315 A58 58 0 0 1 1014 315" stroke="var(--pink)"/>
      <path d="M1014 315 A58 58 0 0 0 1130 315" stroke="var(--orange)"/>
    </g>
    <circle cx="666" cy="380" r="4" fill="var(--purple)"/>

    <!-- input connector dots -->
    <circle cx="128" cy="440" r="6" fill="var(--lime)"/>
    <circle cx="253" cy="440" r="6" fill="var(--teal)"/>
    <circle cx="376" cy="440" r="6" fill="var(--navy)"/>
    <circle cx="500" cy="440" r="6" fill="var(--forest)"/>

    <!-- input icons -->
    <g class="icon-people">
      <circle cx="68" cy="440" r="28" fill="var(--icon-bg)"/>
      <g fill="var(--icon-ink)">
        <circle cx="60" cy="430" r="4"/><circle cx="68" cy="428" r="4.5"/><circle cx="76" cy="430" r="4"/>
        <rect x="55" y="436" width="9" height="15" rx="2"/><rect x="63.5" y="435" width="9" height="17" rx="2"/><rect x="72" y="436" width="9" height="15" rx="2"/>
      </g>
    </g>
    <g class="icon-dollars">
      <circle cx="190" cy="440" r="28" fill="var(--icon-bg)"/>
      <circle cx="190" cy="440" r="14" fill="var(--icon-ink)"/>
      <text x="190" y="446" text-anchor="middle" font-family="Lato, sans-serif" font-weight="700" font-size="17" fill="var(--icon-bg)">$</text>
    </g>
    <g class="icon-ideas">
      <circle cx="315" cy="440" r="28" fill="var(--icon-bg)"/>
      <path d="M305 454 V446 C298 440 300 427 312 425 C324 423 330 432 328 440 L331 446 H327 V452 H319 V454 Z" fill="none" stroke="var(--icon-ink)" stroke-width="2"/>
      <circle cx="314" cy="436" r="4" fill="none" stroke="var(--icon-ink)" stroke-width="1.5"/>
    </g>
    <g class="icon-products">
      <circle cx="438" cy="440" r="28" fill="var(--icon-bg)"/>
      <path d="M438 424 L454 432 L438 440 L422 432 Z" fill="var(--icon-ink)"/>
      <path d="M422 436 L437 444 V457 L422 449 Z" fill="var(--icon-ink)"/>
      <path d="M454 436 L439 444 V457 L454 449 Z" fill="var(--icon-ink)"/>
    </g>
    <g class="icon-members">
      <circle cx="562" cy="440" r="28" fill="var(--icon-bg)"/>
      <g fill="var(--icon-ink)">
        <circle cx="555" cy="432" r="5"/><path d="M545 451 C545 441 565 441 565 451 Z"/>
        <circle cx="566" cy="430" r="4"/>
        <circle cx="572" cy="446" r="7"/>
      </g>
      <path d="M572 442 V450 M568 446 H576" stroke="var(--icon-bg)" stroke-width="2"/>
    </g>

    <!-- process icons -->
    <g class="icon-activity-cycle">
      <circle cx="724" cy="305" r="28" fill="var(--icon-bg)"/>
      <g fill="none" stroke="var(--icon-ink)" stroke-width="2">
        <path d="M724 289 A16 16 0 1 1 708 305"/>
        <path d="M724 294 A11 11 0 1 1 713 305"/>
        <path d="M724 299 A6 6 0 1 1 718 305"/>
      </g>
    </g>
    <g class="icon-report">
      <circle cx="840" cy="200" r="30" fill="var(--icon-bg)"/>
      <rect x="829" y="186" width="22" height="27" rx="2" fill="none" stroke="var(--icon-ink)" stroke-width="2"/>
      <rect x="834" y="183" width="12" height="5" fill="var(--icon-ink)"/>
      <g fill="var(--icon-ink)"><rect x="834" y="202" width="3" height="7"/><rect x="839" y="198" width="3" height="11"/><rect x="844" y="195" width="3" height="14"/></g>
    </g>
    <g class="icon-pulse">
      <circle cx="840" cy="305" r="28" fill="var(--icon-bg)"/>
      <polyline points="824,306 832,306 836,296 841,316 845,300 848,306 856,306" fill="none" stroke="var(--icon-ink)" stroke-width="2"/>
    </g>
    <g class="icon-output">
      <circle cx="956" cy="305" r="28" fill="var(--icon-bg)"/>
      <path d="M962 295 A13 13 0 1 0 962 315" fill="none" stroke="var(--icon-ink)" stroke-width="2.5"/>
      <circle cx="958" cy="305" r="3.5" fill="var(--icon-ink)"/>
      <line x1="958" y1="305" x2="972" y2="305" stroke="var(--icon-ink)" stroke-width="2"/>
      <path d="M968 300 L974 305 L968 310" fill="none" stroke="var(--icon-ink)" stroke-width="2"/>
    </g>
    <g class="icon-gears">
      <circle cx="1072" cy="300" r="34" fill="none" stroke="#ffffff" stroke-width="3"/>
      <circle cx="1072" cy="300" r="28" fill="var(--icon-bg)"/>
      <circle cx="1066" cy="302" r="9" fill="var(--icon-ink)"/>
      <circle cx="1066" cy="302" r="3" fill="var(--icon-bg)"/>
      <circle cx="1080" cy="293" r="6" fill="var(--icon-ink)"/>
      <circle cx="1080" cy="293" r="2" fill="var(--icon-bg)"/>
    </g>
    <g class="icon-monitor">
      <circle cx="1138" cy="262" r="30" fill="var(--icon-bg)"/>
      <rect x="1122" y="248" width="32" height="22" fill="none" stroke="var(--icon-ink)" stroke-width="2"/>
      <polyline points="1127,264 1134,258 1140,261 1149,253" fill="none" stroke="var(--icon-ink)" stroke-width="1.6"/>
      <rect x="1134" y="270" width="8" height="5" fill="var(--icon-ink)"/>
      <rect x="1129" y="275" width="18" height="2" fill="var(--icon-ink)"/>
    </g>
    <circle cx="786" cy="218" r="6" fill="var(--spark)"/>
    <circle cx="840" cy="254" r="6" fill="var(--lime)"/>
    <circle cx="1098" cy="278" r="3" fill="var(--lime)"/>
  </svg>

  <div class="brand">
    <span class="brand-dot"></span>
    <span class="brand-rule"></span>
    <span class="brand-name">TrialSprint™</span>
  </div>

  <h2 class="stage-title" style="left:286px;top:335px;">INPUTS</h2>
  <h2 class="stage-title" style="left:666px;top:200px;">ACTIVITIES</h2>
  <h2 class="stage-title" style="left:920px;top:344px;">OUTPUTS</h2>
  <h2 class="stage-title" style="left:1086px;top:201px;">OUTCOMES</h2>

  <h3 class="input-title" style="left:8px;top:386px;">People</h3>
  <h3 class="input-title" style="left:130px;top:386px;">Dollars</h3>
  <h3 class="input-title" style="left:255px;top:373px;">Repurposing Opportunities</h3>
  <h3 class="input-title" style="left:378px;top:386px;">Products</h3>
  <h3 class="input-title" style="left:502px;top:373px;">Member Resources</h3>

  <ul class="note note-list" style="left:26px;top:486px;width:120px;">
    <li>Researchers (academic<br>and corporate)</li>
    <li>Clinicians</li>
    <li>Venture philanthropists</li>
    <li>Industry professionals</li>
    <li>Research institution staff</li>
    <li>Non-profits funding<br>medical research</li>
    <li>Patients</li>
  </ul>
  <p class="note" style="left:162px;top:486px;width:110px;">Philanthropic funding, industry sponsorship, research institution co-funding</p>
  <p class="note" style="left:286px;top:486px;width:122px;">General repurposing ideas from researchers, clinicians, patients, and bioinformatics and specific repurposing research proposals from researchers, clinicians and industry</p>
  <p class="note" style="left:410px;top:486px;width:100px;">Drugs, Devices, Nutriceuticals, Diagnostics, Therapies</p>
  <p class="note" style="left:534px;top:486px;width:120px;">Regulatory expertise, Legal support, Trial management, Manufacturing, Patient enrollment</p>

  <ul class="note note-list" style="left:901px;top:86px;width:130px;">
    <li>Funded proof of concept clinical trials</li>
    <li>Final preclinical research that leads immediately to clinical trials</li>
    <li>New scientific, clinical, philanthropic, geographic collaborations</li>
    <li>An accelerated path from idea to trial initiation to medical solution</li>
  </ul>
  <ul class="note note-list" style="left:785px;top:403px;width:120px;">
    <li>Conversation forums for all stakeholders</li>
    <li>Requests for Proposals from funders</li>
    <li>Research Project Proposals/Scientific Review and Validation from researchers and clinicians</li>
  </ul>
  <p class="note" style="left:1030px;top:403px;width:115px;">Effective, affordable repurposed treatments for patients in need</p>
</main>
</body>
</html>
```